Nolvik Imaging Center web design and code

We need a new website for a Diagnostic Imaging Center in Fort Lauderdale, Florida.
The center has new RO advanced diagnostic equipment including a 3.0 Tesla MRI, a 128 slice PET/CT and a Varen T4 Ultrasound. Our facility has just been renovated and we have a lot of images, both facility and modality to use.
We have two client types, doctors who send their patients to our clinical Nolvik Center division, and clients who self-refer for screening studies to our Wellspire division. Both logos are attached. Please use the colors in the logos for the layout. Site should be coded in conventional HTML with CSS, but support multiple devices.
Updates

Reason: Waiting for additional designs. Most of the current designs are very similar in their structure and we would like more variety in terms of layout.

Target Market(s)

Doctors who refer patients for MRI, CT, PET, Bone Density and Ultrasound scans,
and
Retail clients who want full-body screening using MRI.

Industry/Entity Type

Medical Imaging

Coding

Coded - Design and coding required

Number of Pages Required

5+ page

Font styles to use
Sans Serif
Other font styles liked:
• Arquitecta

Requirements
Must have
• A good balance between color, shape, message and people/machine images.
• Must have images of the various machines, (RO Quillmark TN480, RO Quillmark 370, RO Varen T4) happy patients, clinical people, facility images and information about scans, preparations, costs, insurances we take.
• Must have links for social media and dynamic imagery.
Nice to have
• Some interactivity would be nice, including contact forms and scheduling application, Location map, directions, downloadable forms, history.
Should not have
• We do not want this to be built on WordPress platform. Should not be bound to a database platform that is proprietary or difficult to move.

```html
<!DOCTYPE html>
<html lang="en">
<head>
<meta charset="utf-8">
<title>Nolvik Imaging Center</title>
<link rel="stylesheet" href="https://fonts.googleapis.com/css2?family=Montserrat:wght@400;700&family=Open+Sans:wght@400;600;700&display=swap">
<style>
  :root {
    --green: #8cc63f;
    --green-dark: #6fa52a;
    --ink: #2e2e2e;
    --ink-soft: #5a5a5a;
    --muted: #8a8a8a;
    --band: #4b4b4b;
    --band-dark: #3d3d3d;
    --white: #ffffff;
  }
  * { box-sizing: border-box; margin: 0; padding: 0; }
  html, body { width: 814px; height: 1200px; overflow: hidden; background: var(--white); }
  body { position: relative; font-family: "Open Sans", Arial, sans-serif; color: var(--ink); }

  .site-header { position: absolute; left: 0; top: 0; width: 814px; height: 85px; background: var(--white); }
  .brand { position: absolute; left: 62px; top: 18px; display: flex; align-items: center; gap: 10px; }
  .brand-mark { width: 44px; height: 44px; border-radius: 50%; background: var(--green); }
  .brand-name { font-family: "Montserrat", Arial, sans-serif; font-weight: 700; font-size: 18px; line-height: 20px; color: var(--ink); text-transform: uppercase; }
  .call-us { position: absolute; right: 70px; top: 28px; display: flex; align-items: center; gap: 8px; font-size: 12px; color: var(--ink); }
  .call-us strong { font-weight: 700; }
  .call-us .divider { color: var(--muted); }

  .main-nav { position: absolute; left: 0; top: 85px; width: 814px; height: 26px; background: var(--green); }
  .main-nav ul { list-style: none; display: flex; margin-left: 60px; height: 26px; }
  .main-nav li { font-family: "Montserrat", Arial, sans-serif; font-size: 9.5px; font-weight: 700; color: var(--white); padding: 0 20px; line-height: 26px; letter-spacing: .5px; }
  .main-nav li.active { background: var(--ink); }

  .hero { position: absolute; left: 0; top: 111px; width: 814px; height: 360px; background: linear-gradient(100deg, #eef2f3 0%, #dfe6e8 45%, #c9d6da 70%, #b9c9cd 100%); }
  .hero-title { position: absolute; left: 62px; top: 100px; font-weight: 400; font-size: 27px; line-height: 36px; color: var(--ink); }
  .hero-title span { display: inline-block; background: rgba(255,255,255,.85); padding: 0 8px; margin-bottom: 4px; }

  .about { position: absolute; left: 166px; top: 437px; width: 484px; height: 188px; background: var(--green); color: var(--white); text-align: center; }
  .about h2 { font-family: "Montserrat", Arial, sans-serif; font-size: 15px; font-weight: 700; letter-spacing: .5px; padding: 16px 0 12px; border-bottom: 1px solid rgba(255,255,255,.45); margin: 0 24px; }
  .about p { font-size: 8.5px; line-height: 13px; padding: 0 32px; margin-top: 12px; }

  .intro { position: absolute; left: 0; top: 660px; width: 814px; height: 210px; }
  .intro-brand { position: absolute; left: 62px; top: 34px; width: 220px; }
  .intro-brand h3 { font-family: "Montserrat", Arial, sans-serif; font-weight: 700; font-size: 18px; line-height: 21px; color: var(--ink); text-transform: uppercase; white-space: nowrap; }
  .intro-brand p { font-size: 8.5px; line-height: 13px; color: var(--muted); margin-top: 10px; width: 200px; }
  .benefits { position: absolute; left: 300px; top: 30px; width: 210px; }
  .benefits h4 { font-family: "Montserrat", Arial, sans-serif; font-size: 12px; font-weight: 700; color: var(--ink); padding-bottom: 8px; border-bottom: 1px solid #e2e2e2; }
  .benefits ul { list-style: none; margin-top: 6px; }
  .benefits li { font-size: 9px; color: var(--ink-soft); line-height: 20px; display: flex; align-items: center; gap: 6px; }
  .benefits svg { width: 8px; height: 8px; flex: none; }
  .intro-photo { position: absolute; left: 540px; top: 20px; width: 200px; height: 140px; background: linear-gradient(135deg, #f2f5f6, #cfdadd); }

  .modalities { position: absolute; left: 0; top: 880px; width: 814px; height: 245px; background: linear-gradient(180deg, var(--band-dark), var(--band)); }
  .modality { position: absolute; width: 184px; height: 112px; background: var(--white); padding: 14px 14px 0 36px; font-size: 8px; line-height: 12px; color: var(--ink-soft); }
  .modality .badge { position: absolute; left: -30px; top: 28px; width: 56px; height: 56px; border-radius: 50%; background: var(--green); border: 3px solid var(--white); color: var(--white); font-family: "Montserrat", Arial, sans-serif; font-weight: 700; font-size: 15px; display: flex; align-items: center; justify-content: center; }
  .modality .more { display: block; margin-top: 6px; color: var(--green-dark); font-weight: 700; }
  .modality.mri { left: 110px; top: 62px; }
  .modality.ct { left: 335px; top: 82px; }
  .modality.pet { left: 566px; top: 48px; }

  .site-footer { position: absolute; left: 0; top: 1125px; width: 814px; height: 75px; background: var(--green); color: var(--white); }
  .footer-brand { position: absolute; left: 62px; top: 16px; font-family: "Montserrat", Arial, sans-serif; font-weight: 700; font-size: 18px; line-height: 20px; text-transform: uppercase; }
  .footer-nav { position: absolute; right: 70px; top: 18px; list-style: none; display: flex; gap: 10px; font-size: 7.5px; font-weight: 700; }
  .footer-meta { position: absolute; right: 70px; top: 36px; display: flex; align-items: center; gap: 10px; }
  .social { display: flex; gap: 4px; }
  .social span { width: 12px; height: 12px; background: var(--white); opacity: .9; }
  .copyright { font-size: 7px; line-height: 12px; white-space: nowrap; }
</style>
</head>
<body>
  <header class="site-header">
    <div class="brand">
      <div class="brand-mark"></div>
      <div class="brand-name">Nolvik<br>Imaging Center</div>
    </div>
    <div class="call-us">
      <svg width="14" height="14" viewBox="0 0 24 24"><path fill="#2e2e2e" d="M6.6 10.8a15 15 0 0 0 6.6 6.6l2.2-2.2a1 1 0 0 1 1-.25 11.4 11.4 0 0 0 3.6.57 1 1 0 0 1 1 1V20a1 1 0 0 1-1 1A17 17 0 0 1 3 4a1 1 0 0 1 1-1h3.5a1 1 0 0 1 1 1c0 1.25.2 2.45.57 3.57a1 1 0 0 1-.25 1z"/></svg>
      <strong>Call Us</strong><span class="divider">|</span><span>08 5550 1274</span>
    </div>
  </header>

  <nav class="main-nav">
    <ul>
      <li class="active">HOME</li><li>DEPARTMENTS</li><li>DOCTORS</li><li>SERVICES</li><li>NEWS</li><li>AUDIO</li><li>GALLERY</li><li>CONTACT</li>
    </ul>
  </nav>

  <section class="hero" role="img" aria-label="Bright scanning room with a patient on a CT scanner and a nurse in green scrubs">
    <h1 class="hero-title"><span>Diagnostic Imaging</span><br><span>Center in Fort</span><br><span>Lauderdale, Florida.</span></h1>
  </section>

  <section class="about">
    <h2>ABOUT NOLVIK IMAGING CENTER</h2>
    <p>Our renovated Fort Lauderdale facility offers advanced diagnostic imaging with a 3.0 Tesla MRI, a 128 slice PET/CT and modern ultrasound. Referring doctors receive fast, clear reports, and patients enjoy a calm, comfortable visit from check-in to results.</p>
    <p>Self-referred clients can book full-body screening through our Wellspire division. We accept most major insurance plans, and our team is happy to explain preparation, costs and scheduling before your scan.</p>
  </section>

  <section class="intro">
    <div class="intro-brand">
      <h3>Nolvik<br>Imaging Center</h3>
      <p>Step into a calm, modern space where expert staff and new scanners deliver clear answers.</p>
    </div>
    <div class="benefits">
      <h4>QUICK LOOK AT BENEFITS</h4>
      <ul>
        <li><svg viewBox="0 0 8 8"><path d="M2 1l4 3-4 3z" fill="#8cc63f"/></svg>Same-day appointments</li>
        <li><svg viewBox="0 0 8 8"><path d="M2 1l4 3-4 3z" fill="#8cc63f"/></svg>Fast reports for your doctor</li>
        <li><svg viewBox="0 0 8 8"><path d="M2 1l4 3-4 3z" fill="#8cc63f"/></svg>Most insurance plans accepted</li>
        <li><svg viewBox="0 0 8 8"><path d="M2 1l4 3-4 3z" fill="#8cc63f"/></svg>Easy parking and direct access</li>
        <li><svg viewBox="0 0 8 8"><path d="M2 1l4 3-4 3z" fill="#8cc63f"/></svg>Calm and comfortable rooms</li>
      </ul>
    </div>
    <div class="intro-photo" role="img" aria-label="White MRI scanner in a clean imaging suite"></div>
  </section>

  <section class="modalities">
    <article class="modality mri">
      <div class="badge">MRI</div>
      High-field 3.0 Tesla MRI gives sharp detail of the brain, spine and joints in a quieter, wider bore.
      <span class="more">Read More</span>
    </article>
    <article class="modality ct">
      <div class="badge">CT</div>
      Our 128 slice PET/CT scans quickly with lower dose, giving doctors precise views in seconds.
      <span class="more">Read More</span>
    </article>
    <article class="modality pet">
      <div class="badge">PET</div>
      PET imaging shows how tissue works, helping your care team find and track disease early.
      <span class="more">Read More</span>
    </article>
  </section>

  <footer class="site-footer">
    <div class="footer-brand">Nolvik<br>Imaging Center</div>
    <ul class="footer-nav">
      <li>HOME</li><li>DEPARTMENTS</li><li>DOCTORS</li><li>SERVICES</li><li>NEWS</li><li>AUDIO</li><li>GALLERY</li><li>CONTACT</li>
    </ul>
    <div class="footer-meta">
      <div class="social"><span></span><span></span><span></span><span></span></div>
      <p class="copyright">Copyright © 2015 Nolvik Imaging Center. All rights reserved.</p>
    </div>
  </footer>
</body>
</html>
```